Golden Years Wellness Map: This is my second book. The first was Elder Care Compass

I need a book cover design for: GOLDEN YEARS WELLNESS MAP: A NO-FEE METHOD FOR FINISHING YOUR LATER-LIFE JIGSAW THROUGH POOLED CARE SAVINGS ACCOUNTS by Derek Follard Ross Pellick & Martin Guvel. This book is designed for business owners, CEO's, CFO's and Human Resources. The cover needs to be professional and focused on business. The purpose of this book is to educate business owners and their management about a zero cost retiree health plan. This is a first of it's kind solution that every business needs to learn about.

Target Market(s)

Business owners, CEO's, CFO's and Human Resources

Requirements
Nice to have
• I want the design to be clean and professional since it is focused on business executives

```html
<!DOCTYPE html>
<html lang="en">
<head>
<meta charset="utf-8">
<title>Golden Years Wellness Map – Book Cover</title>
<link rel="stylesheet" href="https://fonts.googleapis.com/css2?family=Jost:wght@400;500;600&display=swap">
<style>
  :root {
    --stage: #f2f3f5;
    --navy-deep: #0c2370;
    --navy: #163a9c;
    --royal: #1f4fc0;
    --sky: #36a9de;
    --sky-light: #7fc4ee;
    --white: #ffffff;
    --ink: #0b1f4d;
  }
  * { margin: 0; padding: 0; box-sizing: border-box; }
  html, body {
    width: 1200px;
    height: 663px;
    overflow: hidden;
    background: var(--stage);
    font-family: "Jost", "Futura", sans-serif;
  }
  .book-cover {
    position: absolute;
    left: 395px;
    top: 31px;
    width: 410px;
    height: 600px;
    background: linear-gradient(180deg, var(--navy-deep) 0%, var(--navy) 55%, var(--navy-deep) 100%);
    overflow: hidden;
  }
  .cover-photo {
    position: absolute;
    left: 0;
    top: 0;
    width: 100%;
    height: 264px;
    background:
      radial-gradient(ellipse at 45% 60%, #9fb6dc 0%, rgba(159,182,220,0) 35%),
      radial-gradient(ellipse at 70% 30%, #5b8fe0 0%, rgba(91,143,224,0) 45%),
      linear-gradient(160deg, #4d78c9 0%, var(--royal) 45%, var(--navy) 100%);
  }
  .title-block {
    position: absolute;
    left: 0;
    top: 298px;
    width: 100%;
    text-align: center;
    color: var(--white);
  }
  .title-line {
    display: block;
    font-weight: 500;
    font-size: 44px;
    line-height: 48px;
    letter-spacing: 0.08em;
  }
  .title-line--accent { color: var(--sky); }
  .subtitle {
    margin-top: 14px;
    font-size: 11.2px;
    line-height: 18px;
    letter-spacing: 0.07em;
  }
  .subtitle-lead {
    display: block;
    color: var(--sky-light);
    font-weight: 500;
    font-size: 11.6px;
  }
  .subtitle-main {
    display: block;
    font-weight: 600;
  }
  .author-band {
    position: absolute;
    left: 0;
    bottom: 0;
    width: 100%;
    height: 62px;
    background: var(--sky);
    display: flex;
    align-items: center;
    justify-content: center;
  }
  .author-names {
    color: var(--ink);
    font-weight: 600;
    font-size: 12px;
    letter-spacing: 0.06em;
  }
</style>
</head>
<body>
  <main class="book-cover">
    <div class="cover-photo" role="img" aria-label="Photograph of a stethoscope resting on a desk with a glowing heartbeat line, in blue tones"></div>
    <h1 class="title-block">
      <span class="title-line">GOLDEN YEARS</span>
      <span class="title-line">WELLNESS</span>
      <span class="title-line title-line--accent">MAP</span>
      <p class="subtitle">
        <span class="subtitle-lead">A NO-FEE METHOD FOR</span>
        <span class="subtitle-main">FINISHING YOUR LATER-LIFE JIGSAW</span>
        <span class="subtitle-main">THROUGH POOLED CARE SAVINGS ACCOUNTS</span>
      </p>
    </h1>
    <footer class="author-band">
      <p class="author-names">DEREK FOLLARD, ROSS PELLICK &amp; MARTIN GUVEL</p>
    </footer>
  </main>
</body>
</html>
```